Holistic Therapy (aromatherapy, massage, reflexology, life coaching, soul healing, aura reading)

I work for myself as a holistic therapist doing: aromatherapy massage, massage, reflexology, abdominal-sacral massage, life coaching, soul healing, aura readings. I want a business card that doesn't focus on any one of these( so not just feet or a massage couch,but rather a card that creates the feeling of wholeness, healing, health and which can encompass all my therapies - e.g. green or purple are colours I like (especially green, or maybe green on back and purple on front). It's going to be called Rosa Elwin Therapies. I don't want to list all my therapies on the card in case I add others later.). At some point I will create a website but in this instance I just want to get some cards printed to get 'out there' while I design my website.
Updates

Hi, thanks for all your designs. Can you find a way to include the therapies that I offer within the card, either on the front or back…the therapies I offer are: aromatherapy massage, reflexology, swedish body massage, abdominal-sacral massage, nutrition, soul healing, aura readings. (Maybe have them with a bullet point before each?) I am not sure whether they should be on the front of the card or the back or whether having them would spoil the card but it occurred to me that just having rosa elwin therapies doesn't tell people what therapies I offer, hence the new idea to list them somehow…)

Target Market(s)

Mainly women (middle class probably with disposable incomes).

Industry/Entity Type

Massage

Contact Information for Business Card

Rosa Elwin Therapies, Tel: 07942 586113, email: vitalbloom@mailvane.com, (on back of card I want: Rosalind Elwin BScHons, OKQRB, GPCL.)

Requirements
Nice to have
• A logo for Rosa Elwin Therapies would be good.

```html
<!DOCTYPE html>
<html lang="en">
<head>
<meta charset="utf-8">
<title>Rosa Elwin Therapies – Business Card</title>
<link href="https://fonts.googleapis.com/css2?family=Gabriela&family=Open+Sans:wght@400&display=swap" rel="stylesheet">
<style>
  :root {
    --backdrop-top: #d6d6d6;
    --backdrop-bottom: #f7f7f7;
    --card-white: #ffffff;
    --brand-purple: #8a2a8a;
    --brand-purple-deep: #6e1f70;
    --brand-purple-light: #a23ea3;
    --brand-green: #1f8a3a;
    --brand-green-light: #3aa94e;
    --text-light: #ffffff;
  }
  * { box-sizing: border-box; margin: 0; padding: 0; }
  html, body {
    width: 1200px;
    height: 900px;
    overflow: hidden;
  }
  body {
    background: linear-gradient(to bottom, var(--backdrop-top), var(--backdrop-bottom) 60%);
    display: flex;
    align-items: center;
    justify-content: center;
    gap: 50px;
    font-family: "Open Sans", Arial, sans-serif;
  }
  .card {
    position: relative;
    width: 530px;
    height: 310px;
    border-radius: 26px;
    box-shadow: 0 14px 30px rgba(0, 0, 0, 0.18);
  }
  .card-frame {
    position: absolute;
    inset: 12px;
    border-radius: 20px;
    border: 8px solid;
  }

  /* Front */
  .card-front { background: var(--card-white); }
  .card-front .card-frame { border-color: var(--brand-purple); }
  .front-content {
    position: absolute;
    inset: 0;
    display: flex;
    flex-direction: column;
    align-items: center;
    padding-top: 52px;
  }
  .brand-mark {
    width: 92px;
    height: 92px;
    border-radius: 50%;
    background: var(--brand-green);
  }
  .brand-name {
    margin-top: 20px;
    font-family: "Gabriela", Georgia, serif;
    font-size: 27px;
    color: var(--brand-purple);
    letter-spacing: 0.3px;
  }
  .contact {
    margin-top: 16px;
    text-align: center;
    color: var(--brand-green);
    font-size: 19px;
    line-height: 1.2;
  }

  /* Back */
  .card-back {
    background:
      radial-gradient(circle at 52% 38%, rgba(255,255,255,0.55) 0, rgba(255,255,255,0.12) 6%, rgba(255,255,255,0) 22%),
      linear-gradient(160deg, var(--brand-purple-light), var(--brand-purple) 55%, var(--brand-purple-deep));
  }
  .card-back .card-frame { border-color: var(--text-light); }
  .back-content {
    position: absolute;
    inset: 0;
    display: flex;
    align-items: center;
    justify-content: center;
  }
  .practitioner {
    color: var(--text-light);
    font-size: 19px;
    letter-spacing: 0.2px;
  }
</style>
</head>
<body>
  <section class="card card-front" aria-label="Business card front">
    <div class="card-frame"></div>
    <div class="front-content">
      <div class="brand-mark" aria-hidden="true"></div>
      <h1 class="brand-name">Rosa Elwin Therapies</h1>
      <p class="contact">
        <span class="contact-phone">07942 586113</span><br>
        <span class="contact-email">vitalbloom@mailvane.com</span>
      </p>
    </div>
  </section>

  <section class="card card-back" aria-label="Business card back">
    <div class="card-frame"></div>
    <div class="back-content">
      <p class="practitioner">Rosalind Elwin BScHons, OKQRB, GPCL.</p>
    </div>
  </section>
</body>
</html>
```